Stationary design for boutique production house

We need a stationary design for our production house, 'Luma Studios' based in Singapore. We produce microfilms as well as podcasts, talkshows and events. Our logo is a stylized icon of our director, who is also the executive producer and host of our programs, Orla. Our main company colors are Red, Black and white. We would like a clean, minimalist design incorporating our existing company logo that conveys a sense of urbanism and elegance.

Logo and font files are attached. f

Target Market(s)

We focus on lifestyle media rather than entertainment.

Industry/Entity Type

Boutique

Font styles to use
Serif
Sans Serif

Colors
ec1f27
ffffff
000000

Requirements
Must have
• Our company logo and at least one of our company colors.
Nice to have
• Our address and contact information.
Should not have
• Changes made to the company logo (using only certain parts of it is fine though)

```html
<!DOCTYPE html>
<html lang="en">
<head>
<meta charset="utf-8">
<title>Luma Studios Stationery</title>
<link rel="stylesheet" href="https://fonts.googleapis.com/css2?family=Questrial&display=swap">
<style>
:root{
  --red:#ff0613;
  --red-deep:#c10008;
  --ink:#1a1410;
  --paper:#ffffff;
  --paper-soft:#f7f7f7;
  --bg:#eceef0;
  --muted:#b3b3b3;
  --grey-box:#b9b9b9;
}
*{box-sizing:border-box;margin:0;padding:0}
html,body{width:1200px;height:1002px;overflow:hidden}
body{
  background:radial-gradient(ellipse at 55% 45%,#f7f8f9 0%,var(--bg) 75%);
  font-family:"Questrial",Arial,sans-serif;position:relative;
}
.item{position:absolute;box-shadow:0 6px 14px rgba(0,0,0,.18)}
.abs{position:absolute}
.mark{position:absolute;display:flex;flex-direction:column;align-items:center;justify-content:center;gap:4px;text-align:center}
.mark .dot{border-radius:50%}
.mark .name{font-family:"Questrial",Arial,sans-serif;line-height:1.05;letter-spacing:.02em}
.mark.on-white .dot{background:var(--ink)}
.mark.on-white .name{color:var(--ink)}
.mark.on-red .dot{background:var(--paper)}
.mark.on-red .name{color:var(--paper)}
.fine{font-size:6.5px;color:var(--muted);letter-spacing:.08em;white-space:nowrap}

/* folder */
.folder{left:62px;top:149px;width:346px;height:471px;background:var(--paper-soft)}
.folder .band{left:0;top:79px;width:346px;height:290px;background:var(--red)}
.folder .logo-tile{left:239px;top:176px;width:107px;height:96px;background:var(--paper)}

/* letterhead */
.letterhead{left:430px;top:149px;width:334px;height:474px;background:var(--paper)}
.letterhead .logo-tile{left:32px;top:34px;width:61px;height:61px;background:var(--red)}
.letterhead .rule{left:0;bottom:0;width:100%;height:3px;background:var(--red)}
.contact-row{display:flex;gap:12px;align-items:center}
.contact{display:flex;align-items:center;gap:4px}
.icon{width:9px;height:9px;flex:none}

/* business cards */
.card{width:164px;height:94px;background:var(--paper-soft)}
.card.red{background:var(--red)}
.card .edge-top{left:0;top:0;width:100%;height:2px;background:var(--red)}
.card .edge-bottom{left:0;bottom:0;width:100%;height:2px;background:var(--red)}
.card .person{left:10px;top:30px}
.card .person .who{font-size:9px;color:#a9a9a9;letter-spacing:.1em}
.card .person .role{font-size:6.5px;color:#bdbdbd;letter-spacing:.08em;margin-top:1px}
.card .lines{left:78px;top:29px;display:flex;flex-direction:column;gap:9px}
.card .lines .fine{font-size:5px}

/* envelopes */
.env-back{left:83px;top:707px;width:293px;height:139px;background:var(--paper)}
.flap{left:83px;top:656px;width:293px;height:52px}
.env-back .seal{left:124px;top:0;width:44px;height:43px;background:var(--grey-box)}
.env-back .seal .dot{background:var(--paper)}
.env-back .seal .name{color:var(--paper)}
.env-back .line{left:8px;top:122px;width:277px;height:1px;background:#d0d0d0}
.env-front{left:408px;top:707px;width:292px;height:139px;background:var(--paper)}
.env-front .band{left:0;top:70px;width:161px;height:52px;background:var(--red)}
.env-front .logo-tile{left:0;top:75px;width:38px;height:38px;background:var(--paper)}

/* disc sleeve */
.disc{left:900px;top:665px;width:164px;height:164px;border-radius:50%;border:2px solid var(--red);background:var(--paper);box-shadow:0 4px 10px rgba(0,0,0,.12)}
.sleeve{left:823px;top:650px;width:193px;height:192px;background:linear-gradient(180deg,#f50a10 0%,var(--red-deep) 100%)}
.sleeve .logo-tile{left:15px;top:14px;width:58px;height:58px;background:var(--paper)}
</style>
</head>
<body>

<svg width="0" height="0" style="position:absolute">
  <defs>
    <symbol id="ico-mail" viewBox="0 0 10 10"><circle cx="5" cy="5" r="5" fill="#ff0613"/><rect x="2.5" y="3.3" width="5" height="3.4" fill="#fff"/></symbol>
    <symbol id="ico-web" viewBox="0 0 10 10"><circle cx="5" cy="5" r="5" fill="#ff0613"/><circle cx="5" cy="5" r="2.5" fill="none" stroke="#fff" stroke-width="1"/></symbol>
    <symbol id="ico-phone" viewBox="0 0 10 10"><circle cx="5" cy="5" r="5" fill="#ff0613"/><path d="M3.3 2.8l1 .2.4 1.2-.6.5a3.4 3.4 0 0 0 1.4 1.4l.5-.6 1.2.4.2 1-.8.5A4.6 4.6 0 0 1 2.8 3.6z" fill="#fff"/></symbol>
  </defs>
</svg>

<!-- folder -->
<section class="item folder">
  <div class="abs band"></div>
  <div class="abs logo-tile">
    <div class="mark on-white" style="inset:0">
      <span class="dot" style="width:12px;height:12px"></span>
      <span class="name" style="font-size:12px">Luma Studios</span>
    </div>
  </div>
  <div class="abs fine" style="left:20px;top:390px">hello@lumastudios.sg</div>
  <div class="abs fine" style="left:213px;top:390px">address: lorem ipsim 15, h.1</div>
  <div class="abs fine" style="left:20px;top:410px">lumastudios.sg</div>
  <div class="abs fine" style="left:20px;top:429px">65 5550 1234</div>
</section>

<!-- letterhead -->
<section class="item letterhead">
  <div class="abs logo-tile">
    <div class="mark on-red" style="inset:0">
      <span class="dot" style="width:9px;height:9px"></span>
      <span class="name" style="font-size:8px">Luma Studios</span>
    </div>
  </div>
  <div class="abs contact-row" style="left:34px;top:435px">
    <span class="contact"><svg class="icon"><use href="#ico-mail"/></svg><span class="fine">hello@lumastudios.sg</span></span>
    <span class="contact"><svg class="icon"><use href="#ico-web"/></svg><span class="fine">lumastudios.sg</span></span>
    <span class="contact"><svg class="icon"><use href="#ico-phone"/></svg><span class="fine">65 5550 1234</span></span>
  </div>
  <div class="abs rule"></div>
</section>

<!-- business cards -->
<section class="item card red" style="left:804px;top:247px">
  <div class="mark on-red" style="inset:0">
    <span class="dot" style="width:10px;height:10px"></span>
    <span class="name" style="font-size:9px">Luma Studios</span>
  </div>
</section>
<section class="item card" style="left:980px;top:247px">
  <div class="abs edge-top"></div>
  <div class="abs person"><div class="who">Your Name</div><div class="role">Position</div></div>
  <div class="abs lines">
    <span class="contact"><svg class="icon" style="width:8px;height:8px"><use href="#ico-phone"/></svg><span class="fine">65 5550 1234</span></span>
    <span class="contact"><svg class="icon" style="width:8px;height:8px"><use href="#ico-web"/></svg><span class="fine">lumastudios.sg</span></span>
    <span class="contact"><svg class="icon" style="width:8px;height:8px"><use href="#ico-mail"/></svg><span class="fine">hello@lumastudios.sg</span></span>
  </div>
  <div class="abs edge-bottom"></div>
</section>
<section class="item card" style="left:804px;top:365px">
  <div class="abs edge-top" style="background:transparent"></div>
  <div class="mark on-white" style="inset:0">
    <span class="dot" style="width:10px;height:10px"></span>
    <span class="name" style="font-size:9px">Luma Studios</span>
  </div>
  <div class="abs edge-bottom"></div>
</section>
<section class="item card" style="left:982px;top:365px">
  <div class="abs edge-top"></div>
  <div class="abs person"><div class="who">Your Name</div><div class="role">Position</div></div>
  <div class="abs lines">
    <span class="contact"><svg class="icon" style="width:8px;height:8px"><use href="#ico-phone"/></svg><span class="fine">65 5550 1234</span></span>
    <span class="contact"><svg class="icon" style="width:8px;height:8px"><use href="#ico-web"/></svg><span class="fine">lumastudios.sg</span></span>
    <span class="contact"><svg class="icon" style="width:8px;height:8px"><use href="#ico-mail"/></svg><span class="fine">hello@lumastudios.sg</span></span>
  </div>
  <div class="abs edge-bottom"></div>
</section>

<!-- envelope back -->
<section class="item env-back">
  <div class="abs seal">
    <div class="mark" style="inset:0">
      <span class="dot" style="width:7px;height:7px"></span>
      <span class="name" style="font-size:6px">Luma Studios</span>
    </div>
  </div>
  <div class="abs line"></div>
  <div class="abs fine" style="left:0;width:100%;top:126px;text-align:center;font-size:7px">hello@lumastudios.sg</div>
</section>
<svg class="abs flap" viewBox="0 0 293 52" aria-hidden="true">
  <defs><linearGradient id="flapGrad" x1="0" y1="0" x2="0" y2="1"><stop offset="0" stop-color="#ec0a10"/><stop offset="1" stop-color="#c10008"/></linearGradient></defs>
  <path d="M12 0H281Q286 0 287 5L293 52H0L6 5Q7 0 12 0Z" fill="url(#flapGrad)"/>
</svg>

<!-- envelope front -->
<section class="item env-front">
  <div class="abs fine" style="left:8px;top:20px;line-height:1.1">Return Address Line 1<br>Return Address Line 2</div>
  <div class="abs band"></div>
  <div class="abs logo-tile">
    <div class="mark on-white" style="inset:0">
      <span class="dot" style="width:6px;height:6px"></span>
      <span class="name" style="font-size:5.5px">Luma Studios</span>
    </div>
  </div>
  <div class="abs fine" style="left:199px;top:83px;line-height:1.1">Recipient Name<br>Recipient Address Line 1<br>Recipient Address Line 2</div>
</section>

<!-- disc and sleeve -->
<div class="abs disc"></div>
<section class="item sleeve">
  <div class="abs logo-tile">
    <div class="mark on-white" style="inset:0">
      <span class="dot" style="width:8px;height:8px"></span>
      <span class="name" style="font-size:7.5px">Luma Studios</span>
    </div>
  </div>
</section>

</body>
</html>
```